Brackwell Immigration Law

We need a web design for our existing company www.brackwellcounsel.co.uk. We are an immigration consultancy. The final design should communicate professionalism, integrity and affordability.

Industry/Entity Type

It Company

Logo Text

Brackwell Counsel Partners

Number of Pages Required

5+ page

Font styles to use
Serif

Requirements
Must have
• I want to have the same silhouette logo but something different in positioning..
Nice to have
• Please have a look at these websites:
• https://www.travelpathguide.co.uk/visa_uk/
• http://www.oakdenadvisers.co.uk/
• http://www.myrtlegatelaw.org/index.php
• www.brackwellcounsel.co.uk

```html
<!DOCTYPE html>
<html lang="en">
<head>
<meta charset="utf-8">
<title>Brackwell Counsel Partners – Immigration Law</title>
<link rel="stylesheet" href="https://fonts.googleapis.com/css2?family=Open+Sans:wght@400;600;700&display=swap">
<style>
  :root{
    --orange:#f5a11c;
    --orange-deep:#e88a0c;
    --blue:#1c8fe0;
    --brown:#6a3d1f;
    --gold:#d8a323;
    --ink:#2e2218;
    --white:#ffffff;
    --header-bg:rgba(255,255,255,0.82);
  }
  *{box-sizing:border-box;margin:0;padding:0}
  html,body{width:847px;height:1200px;overflow:hidden}
  body{font-family:"Open Sans",Arial,sans-serif;color:var(--white);background:var(--white)}

  .hero{position:relative;height:508px;overflow:hidden}
  .hero-photo{position:absolute;inset:0;
    background:linear-gradient(180deg,#f0b35a 0%,#e9a04a 22%,#c98f5e 45%,#8d7664 62%,#b99a78 78%,#d7b98c 100%)}
  .site-header{position:absolute;top:0;left:0;right:0;height:62px;background:var(--header-bg);
    display:flex;align-items:center;justify-content:space-between;padding-left:18px}
  .brand{display:flex;flex-direction:column;line-height:1}
  .brand-name{font-size:24px;font-weight:700;color:var(--ink)}
  .brand-tag{font-size:11px;font-weight:600;color:var(--ink);margin-top:3px}
  .main-nav{display:flex;align-items:stretch;height:62px}
  .main-nav a{display:flex;align-items:center;padding:0 16px;font-size:10px;font-weight:700;color:var(--ink);text-decoration:none;letter-spacing:.3px}
  .main-nav a.is-active{background:var(--orange);color:var(--white)}
  .nav-tools{display:flex;align-items:center;gap:6px;padding:0 14px 0 8px}
  .tool-btn{width:22px;height:22px;background:var(--orange);display:flex;align-items:center;justify-content:center}

  .hero-caption{position:absolute;right:34px;top:255px;text-align:right}
  .hero-title{font-size:34px;font-weight:600;line-height:1.1;text-transform:uppercase;letter-spacing:.5px;text-shadow:0 1px 3px rgba(0,0,0,.3)}
  .hero-text{display:inline-block;margin-top:10px;font-size:11px;line-height:1.45;color:var(--orange);background:rgba(255,255,255,.75);padding:3px 6px;max-width:430px}
  .btn-light{display:inline-block;margin-top:14px;background:var(--white);color:var(--ink);font-size:11px;font-weight:700;padding:9px 14px;text-decoration:none}
  .slider-dots{position:absolute;right:34px;top:436px;display:flex;gap:6px}
  .slider-dots span{width:8px;height:8px;border-radius:50%;background:rgba(255,255,255,.6)}
  .slider-dots span.is-current{background:var(--white)}

  .band{text-align:center;padding:0 56px}
  .band h2{font-weight:400;font-size:30px}
  .band p{font-size:10.5px;line-height:1.6}
  .btn-outline{display:inline-block;border:1px solid var(--white);color:var(--white);font-size:9px;padding:8px 16px;text-decoration:none}

  .welcome{background:var(--blue);height:232px;padding-top:30px}
  .welcome p{margin:16px 0 20px}
  .services{background:var(--brown);height:276px;padding-top:34px}
  .services h2{margin-bottom:24px}
  .services p{margin-bottom:40px}
  .team{background:var(--gold);height:184px;padding-top:22px}
  .team p{margin:14px 0 24px}
  .team-row{display:flex;justify-content:space-around;padding:0 40px}
  .member-photo{width:100px;height:100px;border-radius:50%;border:3px solid var(--white);
    background:linear-gradient(160deg,#d9d2c7,#8b8177)}
</style>
</head>
<body>
  <section class="hero">
    <div class="hero-photo" role="img" aria-label="City skyline at sunset with a person relaxing on a bench in the foreground"></div>
    <header class="site-header">
      <div class="brand">
        <span class="brand-name">Brackwell Counsel Partners</span>
        <span class="brand-tag">Immigration Law</span>
      </div>
      <nav class="main-nav">
        <a href="#" class="is-active">HOME</a>
        <a href="#">ABOUT US</a>
        <a href="#">VISA'S</a>
        <a href="#">BLOG</a>
        <a href="#">CONTACT US</a>
        <div class="nav-tools">
          <span class="tool-btn" aria-label="Search">
            <svg width="11" height="11" viewBox="0 0 12 12"><circle cx="5" cy="5" r="3.5" fill="none" stroke="#fff" stroke-width="1.6"/><line x1="7.6" y1="7.6" x2="11" y2="11" stroke="#fff" stroke-width="1.8"/></svg>
          </span>
          <span class="tool-btn" aria-label="Email">
            <svg width="12" height="9" viewBox="0 0 12 9"><rect x=".5" y=".5" width="11" height="8" fill="none" stroke="#fff"/><polyline points=".5,.5 6,5 11.5,.5" fill="none" stroke="#fff"/></svg>
          </span>
        </div>
      </nav>
    </header>
    <div class="hero-caption">
      <h1 class="hero-title">Consectetur adipiscing<br>lorem ipsum dolor</h1>
      <p class="hero-text">Lorem ipsum dolor sit amet, consectetur adipiscing elit, sed do eiusmod<br>tempor incididunt ut labore et dolore magna aliqua</p><br>
      <a href="#" class="btn-light">READ MORE</a>
    </div>
    <div class="slider-dots"><span class="is-current"></span><span></span><span></span></div>
  </section>

  <section class="band welcome">
    <h2>Welcome to Brackwell Counsel Partners</h2>
    <p>Lorem ipsum dolor sit amet, consectetur adipiscing elit, sed do eiusmod tempor incididunt ut labore et dolore magna aliqua. Ut enim ad minim veniam, quis nostrud exercitation ullamco laboris nisi ut aliquip ex ea commodo consequat. Duis aute irure dolor in reprehenderit in voluptate velit esse cillum dolore eu fugiat nulla pariatur. Excepteur sint occaecat cupidatat non proident, sunt in culpa qui officia deserunt mollit anim id est laborum. Sed ut perspiciatis unde omnis iste natus error sit voluptatem accusantium doloremque laudantium, totam rem aperiam, eaque ipsa quae ab illo inventore veritatis et quasi architecto beatae vitae dicta sunt explicabo.</p>
    <a href="#" class="btn-outline">Read More</a>
  </section>

  <section class="band services">
    <h2>Our Services</h2>
    <p>We specialise in all sorts of immigration matters such as Entry Clearance Applications if you want to bring your family from abroad, Dependant visas, Work Permits, Student Visas, Marriage and Civil Partnership visas, Immigration Appeals at the Tribunal and Advocacy, Reconsideration Hearings, Immigration Detention and Applications for Regularisation of Stay and leave to remain, Applications such as Permanent Residency, Citizenship, Renewals of Visas and Visa Extension Applications.</p>
    <a href="#" class="btn-outline">Read More</a>
  </section>

  <section class="band team">
    <h2>Our Team</h2>
    <p>We are immigration advisers regulated at the highest level and accredited by the national law society. We are members of leading practitioner associations and work with councils for the welfare of immigrants.</p>
    <div class="team-row">
      <div class="member-photo" role="img" aria-label="Portrait of team member in a suit"></div>
      <div class="member-photo" role="img" aria-label="Portrait of team member in a suit"></div>
      <div class="member-photo" role="img" aria-label="Portrait of team member in a suit"></div>
      <div class="member-photo" role="img" aria-label="Portrait of team member in a suit"></div>
    </div>
  </section>
</body>
</html>
```